lunetra.com redesign

We are a successful web hosting company that has been around since 1999 with 10,000 customers managing 2,000 websites and 12,000 domain names. Our challenge - we are losing ground because our site is getting old, our pricing is not competitive and our feature set needs to change to match the new world of mobile centric everything. We want to reach out to all of the domain names that we don't host websites for. We believe that if we designed a new site that focuses on bringing home all of those externally hosted websites to our own web hosting company that we would have a solid future. We need to compete against mopwizzle.com, vantrimble.com, kerbloom.com, zinqhut.com, nolvark.com, brimfolk.com, quorvane.com, welbix.com and 100,000 others. We need to simplify our message with clean design, focused pages, easy decision making processes for the consumer. We use WHMCS for the background provisioning and billing so we can pretty much manage any kind of pricing model and discounted promotion packages.
I would prefer Chirpline bootstrap CSS based responsive design.

Reason: I was away on vacation for 2 weeks - I just got back - I need time to fairly review all submissions - thank you for your patience. Dorian Fenwick Lunetra.com

Thanks to all who submitted sample designs - unfortunately most of them were nothing much more than already available templates with some of my current content and logo added to them. I will try to be more specific to reduce the number of choices. I need the template be fully compatible with WHMCS and Wordpress if you can't make it work with WHMCS directly. Another question I have to ask is -"exactly what am I getting for my $500.00 - is it just a PSD template or actual integration of that theme into WHMCS or Wordpress?"  I don't expect anyone to create new content for the site at that price. What do you charge if  you are able to create content or get directly involved in the site implementation of that template?

```html
<!DOCTYPE html>
<html lang="en">
<head>
<meta charset="utf-8">
<title>Lunetra – Web Hosting</title>
<link href="https://fonts.googleapis.com/css2?family=Open+Sans:wght@300;400;600;700;800&display=swap" rel="stylesheet">
<style>
:root{
  --blue:#27a3e3;
  --blue-dark:#1682c0;
  --ink:#333;
  --muted:#888;
  --line:#e3e3e3;
  --panel:#f3f3f3;
  --topbar:#3b3b3b;
  --footer:#2e2e2e;
  --footer-deep:#232323;
  --white:#fff;
}
*{box-sizing:border-box;margin:0;padding:0}
html,body{width:1200px;height:2546px;overflow:hidden}
body{font-family:"Open Sans",Arial,sans-serif;color:var(--ink);background:var(--white);font-size:12px;position:relative}
.wrap{width:892px;margin:0 auto;position:relative;height:100%}
.abs{position:absolute}
ul{list-style:none}

/* top bar */
.topbar{height:24px;background:var(--topbar);color:#bbb;font-size:10px}
.topbar .date{position:absolute;left:8px;top:5px}
.topbar .contact{position:absolute;left:376px;top:5px;display:flex;gap:14px;align-items:center}
.topbar .dots{display:flex;gap:6px}
.topbar .dots i{width:9px;height:9px;border-radius:50%;background:#888;display:block}
.topbar .country{position:absolute;right:0;top:4px;display:flex;gap:5px;align-items:center}
.topbar .country span.sel{background:#eee;color:#333;padding:0 20px 0 4px;height:15px;line-height:15px;font-size:9px;position:relative}
.topbar .country span.sel:after{content:"";position:absolute;right:0;top:0;width:14px;height:15px;background:#555}

/* header */
.header{height:93px;background:linear-gradient(#fff,#f4f4f4);border-bottom:1px solid #ddd}
.logo{position:absolute;left:0;top:20px;font-size:46px;font-weight:800;letter-spacing:-2px;color:#333}
.nav{position:absolute;right:0;top:0;display:flex;height:92px}
.nav a{display:block;padding:0 14px;line-height:72px;font-size:12px;font-weight:600;color:#333;text-decoration:none;border-left:1px solid #e6e6e6}
.nav a.active{color:var(--blue);border-top:3px solid var(--blue);line-height:66px}
.gear{position:absolute;left:0;top:79px;width:38px;height:36px;background:#222;z-index:2;display:flex;align-items:center;justify-content:center}

/* hero */
.hero{height:437px;background:radial-gradient(circle at 60% 40%,#39b4ef,#1d92d4 75%);border-bottom:4px solid #2a2a2a;color:#fff}
.hero h1{position:absolute;left:0;top:42px;font-size:60px;font-weight:600;letter-spacing:0}
.hero h2{position:absolute;left:4px;top:120px;font-size:23px;font-weight:600}
.hero p.lead{position:absolute;left:4px;top:153px;width:470px;font-size:16px;line-height:22px;font-weight:600}
.hero ul{position:absolute;left:4px;top:212px}
.hero li{height:27px;font-size:13px;font-weight:600;display:flex;align-items:center;gap:10px}
.hero li svg{flex:none}
.btn-light{position:absolute;left:5px;top:359px;width:132px;height:35px;background:#fff;color:#1a78b0;border-radius:3px;font-size:12px;font-weight:600;display:flex;align-items:center;justify-content:center;gap:8px;box-shadow:0 2px 3px rgba(0,0,0,.2)}
.hero .servers{position:absolute;left:497px;top:106px;width:395px;height:266px;border-radius:10px;background:linear-gradient(135deg,#3a3a3a,#111 60%,#2b2b2b)}

/* section heads */
.sec-title{font-size:15px;font-weight:700;color:#333;text-transform:uppercase}
.sec-sub{font-size:10px;color:var(--muted);margin-top:2px}

/* services */
.services{height:291px;border-bottom:1px solid var(--line)}
.svc-box{position:absolute;width:280px;height:80px;border:1px solid var(--line);box-shadow:0 1px 2px rgba(0,0,0,.06);background:#fff}
.svc-box .pic{position:absolute;left:14px;top:14px;width:66px;height:52px;border-radius:6px;background:linear-gradient(#d9e6ef,#a9b8c4)}
.svc-box h4{position:absolute;left:114px;top:14px;font-size:12px;font-weight:600;text-transform:uppercase}
.svc-box p{position:absolute;left:114px;top:34px;width:156px;font-size:11px;line-height:16px;color:#777}
.news{position:absolute;left:612px;top:82px;width:280px;height:181px;border:1px solid var(--line);background:#fff}
.news .item{position:absolute;left:18px;width:250px;height:60px}
.news .pic{position:absolute;left:0;top:4px;width:60px;height:46px;border-radius:4px;background:linear-gradient(#cfdbe4,#95a7b6)}
.news h5{position:absolute;left:70px;top:2px;font-size:11px;font-weight:600;text-transform:uppercase}
.news p{position:absolute;left:70px;top:20px;font-size:10.5px;line-height:15px;color:#777}

/* plans */
.plans{height:369px;background:#f4f4f4;border-bottom:1px solid var(--line)}
.plans .vlabel{position:absolute;left:-5px;top:20px;width:20px;height:250px;writing-mode:vertical-rl;transform:rotate(180deg);font-size:18px;font-weight:700;color:#d8d8d8;letter-spacing:2px;text-align:center}
.plan{position:absolute;top:29px;width:200px;height:312px;background:#fff;box-shadow:0 1px 3px rgba(0,0,0,.12)}
.plan .head{height:57px;background:var(--blue);display:flex;color:#fff;position:relative}
.plan .head:after{content:"";position:absolute;left:26px;bottom:-7px;border:7px solid transparent;border-bottom:0;border-top-color:var(--blue-dark)}
.plan .price{width:64px;background:var(--blue-dark);padding:10px 0 0 9px;font-size:18px;font-weight:700;line-height:18px}
.plan .price small{display:block;font-size:7px;font-weight:400;line-height:9px}
.plan .name{padding:12px 0 0 14px;font-size:15px;font-weight:600;line-height:17px;text-transform:uppercase}
.plan ul{padding:18px 0 0 24px}
.plan li{height:24px;font-size:11px;color:#666}
.plan li:before{content:"›";margin-right:6px;color:#999}
.plan .btn{position:absolute;left:25px;top:257px;width:150px;height:34px;background:#444;color:#fff;border-radius:3px;font-size:12px;display:flex;align-items:center;justify-content:center}

/* about */
.about{height:552px}
.intro{position:absolute;left:0;top:30px;width:585px;height:176px;border:1px solid var(--line);background:#fff}
.intro .person{position:absolute;left:16px;top:6px;width:164px;height:168px;background:linear-gradient(#f0f0f0,#c9c9c9);border-radius:4px}
.intro h3{position:absolute;left:220px;top:22px;font-size:15px;font-weight:700;text-transform:uppercase}
.intro p{position:absolute;left:220px;top:46px;width:350px;font-size:11px;line-height:19.5px;color:#666}
.faq{position:absolute;left:612px;top:30px;width:280px;border:1px solid var(--line);background:#fff}
.faq .q{height:42px;display:flex;align-items:center;gap:10px;padding-left:16px;font-size:12px;color:#555;border-top:1px solid var(--line)}
.faq .q:first-child{border-top:0;color:var(--blue)}
.faq .q b{width:15px;height:15px;background:#ddd;color:#fff;font-size:13px;line-height:15px;text-align:center;font-weight:700}
.faq .q:first-child b{background:var(--blue)}
.faq .a{padding:0 16px 14px 42px;font-size:11px;line-height:17px;color:#999}
.card{position:absolute;top:231px;width:280px;height:295px;background:var(--panel)}
.card h3{position:absolute;left:22px;top:20px;font-size:16px;font-weight:700;text-transform:uppercase}
.card ul.inc{position:absolute;left:24px;top:56px}
.card ul.inc li{height:37.5px;display:flex;align-items:center;gap:16px;font-size:11.5px;font-weight:600}
.card ul.inc li i{width:17px;height:17px;border-radius:3px;background:#555;display:block}
.card .devices{position:absolute;left:22px;top:58px;width:236px;height:128px;background:linear-gradient(#f8f8f8,#cfcfcf);border-radius:4px}
.card ul.steps{position:absolute;left:24px;top:214px}
.card ul.steps li{height:21px;font-size:11px;font-weight:600}
.card ul.steps li:before{content:"›";margin-right:8px}
.promo{position:absolute;left:612px;top:248px;width:280px;height:106px;background:#e9e9e9;border:1px solid #ddd;text-align:center}
.promo .just{margin-top:14px;font-size:14px;font-weight:600}
.promo .just sup{font-size:8px}
.promo .save{font-size:27px;font-weight:700;color:var(--blue);line-height:30px}
.promo .save small{font-size:8px;color:#333;font-weight:400}
.promo .tlds{display:flex;justify-content:center;gap:4px;font-size:10px;margin-top:4px;align-items:center}
.promo .tlds span.t{background:#333;color:#fff;padding:1px 4px}

/* why + testimonials */
.why{height:296px;background:#f5f5f5;border-top:1px solid var(--line)}
.why h3{position:absolute;top:28px;font-size:16px;font-weight:700;text-transform:uppercase}
.why .box{position:absolute;top:51px;height:214px;background:#fff;border:1px solid var(--line)}
.why .cols{position:absolute;left:22px;top:14px;display:grid;grid-template-columns:210px 180px}
.why .cols div{height:37.5px;display:flex;align-items:center;gap:12px;font-size:11px;font-weight:600}
.why .cols i{width:20px;height:16px;background:#666;border-radius:3px;display:block}
.quote{position:absolute;left:30px;top:26px;width:370px;font-size:11px;line-height:18px;color:#666;text-align:center}
.quote:before{content:"“";position:absolute;left:-14px;top:-18px;font-size:46px;color:#ddd}
.quote:after{content:"”";position:absolute;right:-14px;top:44px;font-size:46px;color:#ddd}
.who{position:absolute;left:76px;top:138px;text-align:right;font-size:10.5px;font-weight:600;width:122px}
.who small{display:block;font-size:8px;color:#999;font-weight:400}
.avatar{position:absolute;left:210px;top:122px;width:90px;height:90px;background:linear-gradient(#e7e7e7,#b8b8b8)}
.pager{position:absolute;right:30px;top:180px;display:flex;gap:4px}
.pager i{width:7px;height:7px;border-radius:50%;background:#ccc;display:block}

/* tweet bar */
.tweetbar{height:50px;background:var(--blue);color:#fff;margin-top:5px;position:relative}
.tweetbar .bird{position:absolute;left:154px;top:8px;width:34px;height:34px;border-radius:50%;background:#fff}
.tweetbar .arrow{position:absolute;left:210px;top:0;width:24px;height:50px;background:var(--blue-dark);clip-path:polygon(0 0,60% 0,100% 50%,60% 100%,0 100%)}
.tweetbar p{position:absolute;left:252px;top:12px;font-size:9.5px;font-weight:600}
.tweetbar p small{display:block;font-weight:400;font-size:8px;opacity:.85;margin-top:2px}

/* footer */
.footer{height:374px;background:var(--footer);color:#aaa}
.fcol{position:absolute;top:40px}
.fcol h4{color:#fff;font-size:15px;font-weight:600;text-transform:uppercase;margin-bottom:16px}
.fcol p.about-txt{width:155px;font-size:11px;line-height:17.5px;color:#888}
.blog{display:flex;gap:12px;height:50px;margin-bottom:2px}
.blog .thumb{width:44px;height:38px;background:linear-gradient(#cfcfcf,#8a8a8a);flex:none}
.blog h6{font-size:11.5px;font-weight:600;color:#ddd;line-height:15px}
.blog small{font-size:8px;color:#777}
.links li{height:24px;font-size:11px;color:#999}
.links li:before{content:"›";margin-right:6px}
.addr{font-size:11px;line-height:17px;color:#999;width:160px}
.clist li{height:24px;font-size:11px;color:#999;display:flex;align-items:center;gap:10px}
.clist i{width:10px;height:10px;background:#777;display:block;border-radius:2px}
.socials{display:grid;grid-template-columns:repeat(4,29px);gap:7px}
.socials i{width:29px;height:29px;border-radius:50%;background:#555;display:block}
.livechat{margin-top:24px;width:140px;height:42px;background:#444;border-radius:3px;color:#fff;font-size:15px;font-weight:600;display:flex;align-items:center;justify-content:center;gap:10px}
.livechat i{width:22px;height:16px;border-radius:50%;background:#bbb;display:block}
.news-row{position:absolute;left:0;top:300px;width:892px;height:46px;display:flex;align-items:center}
.news-row .env{width:22px;height:16px;background:#666;margin-right:18px}
.news-row .lbl{color:#fff;font-size:12px;font-weight:600;line-height:14px;text-transform:uppercase;width:100px}
.news-row .inp{width:218px;height:30px;background:#1d1d1d;color:#666;font-size:10px;padding:9px 10px}
.news-row .sub{width:80px;height:30px;background:var(--blue);color:#fff;font-size:11px;font-weight:600;display:flex;align-items:center;justify-content:center}
.news-row .cl{margin-left:40px;color:#fff;font-size:11px;font-weight:600;line-height:14px;width:100px}
.partners{display:flex;gap:30px;color:#999;font-size:19px;font-weight:600}
.bottom{height:60px;background:var(--footer-deep);color:#888;font-size:9.5px}
.bottom .l{position:absolute;left:0;top:26px}
.bottom .r{position:absolute;right:0;top:26px}
</style>
</head>
<body>

<div class="topbar"><div class="wrap">
  <span class="date">March 26, 2014</span>
  <div class="contact">
    <span>Live chat</span><span>hello@lunetra.com</span><span>555-210-4477</span>
    <span class="dots"><i></i><i></i><i></i><i></i><i></i></span>
  </div>
  <div class="country"><span>Country:</span><span class="sel">United States</span></div>
</div></div>

<div class="gear"><svg width="18" height="18" viewBox="0 0 18 18"><circle cx="9" cy="9" r="6" fill="none" stroke="#fff" stroke-width="3" stroke-dasharray="3 2"/><circle cx="9" cy="9" r="2" fill="#fff"/></svg></div>

<header class="header"><div class="wrap">
  <div class="logo">lunetra</div>
  <nav class="nav">
    <a class="active">HOME</a><a>WEB HOSTING</a><a>FEATURES</a><a>SERVICES</a><a>BLOG</a><a>SUPPORT</a><a>CONTACT</a>
  </nav>
</div></header>

<section class="hero"><div class="wrap">
  <h1>ADVANCED HOST</h1>
  <h2>SIMPLY DUMMY TEXT FOR PRINTING TYPE</h2>
  <p class="lead">Internet tend to repeat predefined chunks as necessary making this the first true generator on the internet.</p>
  <ul>
    <li><svg width="15" height="15"><circle cx="7.5" cy="7.5" r="7.5" fill="#fff"/><path d="M4 7.5l2.5 2.5 4.5-5" stroke="#1d92d4" stroke-width="2" fill="none"/></svg>Unlimited Bandwidth with Massive Storage</li>
    <li><svg width="15" height="15"><circle cx="7.5" cy="7.5" r="7.5" fill="#fff"/><path d="M4 7.5l2.5 2.5 4.5-5" stroke="#1d92d4" stroke-width="2" fill="none"/></svg>Unlimited Databases and Email Addresses</li>
    <li><svg width="15" height="15"><circle cx="7.5" cy="7.5" r="7.5" fill="#fff"/><path d="M4 7.5l2.5 2.5 4.5-5" stroke="#1d92d4" stroke-width="2" fill="none"/></svg>99.99% Uptime Guarantee &amp; 24/7 Live Support</li>
    <li><svg width="15" height="15"><circle cx="7.5" cy="7.5" r="7.5" fill="#fff"/><path d="M4 7.5l2.5 2.5 4.5-5" stroke="#1d92d4" stroke-width="2" fill="none"/></svg>Apps Including Pressly, Drupo and Joomix</li>
    <li><svg width="15" height="15"><circle cx="7.5" cy="7.5" r="7.5" fill="#fff"/><path d="M4 7.5l2.5 2.5 4.5-5" stroke="#1d92d4" stroke-width="2" fill="none"/></svg>Easy to use Website Builder &amp; one-click Setup</li>
  </ul>
  <div class="btn-light">VIEW DETAILS <svg width="8" height="10"><path d="M1 1l5 4-5 4" stroke="#1a78b0" stroke-width="2" fill="none"/></svg></div>
  <div class="servers" role="img" aria-label="Two black hosting server towers with green lights"></div>
</div></section>

<section class="services"><div class="wrap">
  <div class="abs" style="left:0;top:28px"><div class="sec-title">Make your web site visible to the world</div><div class="sec-sub">Fast and flexible website creator is the easy way to build and manage a site for your business</div></div>
  <div class="svc-box" style="left:0;top:82px"><div class="pic" role="img" aria-label="Computer monitor with globe"></div><h4>Host your website</h4><p>Makings of this the first true generator on the internet.</p></div>
  <div class="svc-box" style="left:305px;top:82px"><div class="pic" role="img" aria-label="At sign emblem for domain names"></div><h4>Domain names</h4><p>Makings of this the first true generator on the internet.</p></div>
  <div class="svc-box" style="left:0;top:182px"><div class="pic" role="img" aria-label="Computer connected to cloud"></div><h4>Cloud servers</h4><p>Makings of this the first true generator on the internet.</p></div>
  <div class="svc-box" style="left:305px;top:182px"><div class="pic" role="img" aria-label="Crossed tools"></div><h4>Hosting solutions</h4><p>Makings of this the first true generator on the internet.</p></div>
  <div class="abs" style="left:612px;top:28px"><div class="sec-title">What's new at Lunetrahost</div><div class="sec-sub">Web hosting services offers and new features</div></div>
  <div class="news">
    <div class="item" style="top:18px"><div class="pic" role="img" aria-label="Laptop for web design services"></div><h5>Web designing services</h5><p>We offer web design services for<br>your businesses and personals.</p></div>
    <div class="item" style="top:102px"><div class="pic" role="img" aria-label="Handshake for affiliate program"></div><h5>Join affiliate program!</h5><p>Affiliates get higher commission<br>Become an affiliate today.</p></div>
  </div>
</div></section>

<section class="plans"><div class="wrap">
  <div class="vlabel">WEB HOSTING PLANS</div>
  <div class="plan" style="left:26px"><div class="head"><div class="price">$ 2.99<small>per month</small></div><div class="name">Standard<br>Hosting</div></div>
    <ul><li>500 GB Disk Space</li><li>100 Databases List</li><li>Free Domain Registration</li><li>1 Hosting Space</li><li>FREE Ad Coupons</li><li>Account Control Panel</li><li>FREE 24/7 Support</li></ul><div class="btn">SIGN UP NOW!</div></div>
  <div class="plan" style="left:247px"><div class="head"><div class="price">$ 4.99<small>per month</small></div><div class="name">Professional<br>Hosting</div></div>
    <ul><li>Unlimited Disk Space</li><li>100 Databases List</li><li>Free Domain Registration</li><li>1 Hosting Space</li><li>FREE Ad Coupons</li><li>Account Control Panel</li><li>FREE 24/7 Support</li></ul><div class="btn">SIGN UP NOW!</div></div>
  <div class="plan" style="left:468px"><div class="head"><div class="price">$ 45<small>per month</small></div><div class="name">Advanced<br>Hosting</div></div>
    <ul><li>Unlimited Disk Space</li><li>100 Databases List</li><li>Free Domain Registration</li><li>1 Hosting Space</li><li>FREE Ad Coupons</li><li>Account Control Panel</li><li>FREE 24/7 Support</li></ul><div class="btn">SIGN UP NOW!</div></div>
  <div class="plan" style="left:689px"><div class="head"><div class="price">$ 99<small>per month</small></div><div class="name">Unlimited<br>Hosting</div></div>
    <ul><li>Unlimited Disk Space</li><li>100 Databases List</li><li>Free Domain Registration</li><li>1 Hosting Space</li><li>FREE Ad Coupons</li><li>Account Control Panel</li><li>FREE 24/7 Support</li></ul><div class="btn">SIGN UP NOW!</div></div>
</div></section>

<section class="about"><div class="wrap">
  <div class="intro">
    <div class="person" role="img" aria-label="Businessman in a suit holding a small plant"></div>
    <h3>We'll just take care of it for you!</h3>
    <p>We will provide you with a hassle free web hosting service where we we take care. The majority have suffered alterations in some form injected humour, or randomised words which dont look the even slightly believable. If you are going to use a passagea lorem Ipsum you need to be sure there anythin embaras middle desktop publishing software like Layoutr Studio including versions.</p>
  </div>
  <div class="faq">
    <div class="q"><b>−</b>What is web hosting?</div>
    <div class="a">There are many variations of passages of Lorem Ipsum available but the</div>
    <div class="q"><b>+</b>What is a domain name?</div>
    <div class="q"><b>+</b>How do I create my web site?</div>
  </div>
  <div class="card" style="left:0">
    <h3>What's included ?</h3>
    <ul class="inc">
      <li><i></i>Free Website Builde</li><li><i></i>Free Domain Registration</li><li><i></i>Free Instant Setup!</li>
      <li><i></i>e-Commerce Shop Carts</li><li><i></i>Free Email Accounts</li><li><i></i>Panelo &amp; Hostdesk Control Panel</li>
    </ul>
  </div>
  <div class="card" style="left:305px">
    <h3>Creating a new website?</h3>
    <div class="devices" role="img" aria-label="Laptop, tablet and phone showing a website, labelled Go Mobile Instantly"></div>
    <ul class="steps"><li>Get Building Started in 3 Easy Steps</li><li>Login to our Hosting Site Builder</li><li>Lorem Ipsum is Simply Dummy text</li></ul>
  </div>
  <div class="promo">
    <div class="just">JUST $9.99<sup>/YEAR*</sup></div>
    <div class="save">SAVE BIG <small>/ ON DOMAINS</small></div>
    <div class="tlds"><span class="t">.com</span><span class="t">.net</span><span>just 7.99 only</span></div>
  </div>
</div></section>

<section class="why"><div class="wrap">
  <h3 style="left:0">Why choose us?</h3>
  <div class="box" style="left:0;width:429px">
    <div class="cols">
      <div><i></i>Domain Registration</div><div><i></i>Cloud Host Servers</div>
      <div><i></i>Web Hosting Services</div><div><i></i>Apps Installs Easy</div>
      <div><i></i>Reseller Web Hosting</div><div><i></i>Money Back Guarantee</div>
      <div><i></i>Virtual Servers</div><div><i></i>Secure Your Web site</div>
      <div><i></i>Dedicated Hosting</div><div><i></i>Quality 24/7 Support</div>
    </div>
  </div>
  <h3 style="left:463px">What people say's</h3>
  <div class="box" style="left:463px;width:429px">
    <p class="quote">There are many variations of passages of Ipsum available but the randomise words which don't look even slightly believable. there isn't anything hidden when looking desktop you need to be sure there isn't anything publishing packages in the middle of generators.</p>
    <div class="who">- Colin Ashby<small>customer</small></div>
    <div class="avatar" role="img" aria-label="Portrait of the quoted customer"></div>
    <div class="pager"><i></i><i></i></div>
  </div>
</div></section>

<div class="tweetbar">
  <div class="bird"></div><div class="arrow"></div>
  <p>As an NRCA-accredited registrar for more than 10 years, Lunetra is a leading provider of domain registration, website hosting, website design, and email
  <small>~ 9 days ago · reply · retweet · favorite</small></p>
</div>

<footer class="footer"><div class="wrap">
  <div class="fcol" style="left:0"><h4>About Lunetra</h4><p class="about-txt">All the you need to be sure there isn't anything embarr assing hiddens the middle text lorempsum generators on the internet tend to the repeat predefined chunks as necessary, making this the first true generator on the internet versions have evolved over the years.</p></div>
  <div class="fcol" style="left:182px"><h4>Recent blogs</h4>
    <div class="blog"><div class="thumb" role="img" aria-label="Blog photo"></div><div><h6>Internet repeat<br>define chunks</h6><small>June 27, 2013</small></div></div>
    <div class="blog"><div class="thumb" role="img" aria-label="Blog photo"></div><div><h6>Majority have<br>super ateration</h6><small>June 26, 2013</small></div></div>
    <div class="blog"><div class="thumb" role="img" aria-label="Blog photo"></div><div><h6>Many desktop<br>push packages</h6><small>June 25, 2013</small></div></div>
  </div>
  <div class="fcol" style="left:364px"><h4>Support &amp; Help</h4>
    <ul class="links"><li>Support &amp; FAQ</li><li>Knowledge Base</li><li>E-mail our Support Team</li><li>My Account &amp; Sign Up</li><li>Submit Ticket</li><li>Video Tutorials</li><li>Hosting Industry News</li></ul>
  </div>
  <div class="fcol" style="left:547px"><h4>Contact us</h4>
    <p class="addr">414 Fernhollow Lane,<br>Brackton, Oregon<br>97310-2044</p>
    <ul class="clist" style="margin-top:10px"><li><i></i>555-210-4477</li><li><i></i>555-210-4478</li><li><i></i>mail@lunetra.com</li><li><i></i>sales@lunetra.com</li></ul>
  </div>
  <div class="fcol" style="left:729px"><h4>Fallow us</h4>
    <div class="socials"><i></i><i></i><i></i><i></i><i></i><i></i><i></i><i></i></div>
    <div class="livechat"><i></i>LIVE CHAT</div>
  </div>
  <div class="news-row">
    <div class="env"></div><div class="lbl">Newsletter<br>Sign up</div>
    <div class="inp">Enter your email address</div><div class="sub">SUBSCRIBE</div>
    <div class="cl">OUR CLIENTS<br>PARTNERS</div>
    <div class="partners"><span>Porvella</span><span>Tandrix</span><span>Quelmo</span></div>
  </div>
</div></footer>

<div class="bottom"><div class="wrap">
  <span class="l">Terms of Service | Privacy Policy | Copyright | Site Map</span>
  <span class="r">Copyright © 2014 Lunetra. All rights reserved</span>
</div></div>

</body>
</html>
```